Clever & creative business card needed for a pediatric dentist.

We need a business card for a pediatric dentist that is building a brand-new pediatric dental practice. He is funny, outgoing, and sociable, and he hopes to give his business card to dentists and pediatricians so that he can give them information of where to refer infants, children, and teenagers that need high quality and attainable dental care.

The name of the dental practice is Copper Fern Pediatric Dentistry. Logo design .png / .pdf/ .jpg are provided to aid in the design.

The dentist's last name is Tolvan (which sounds like "burger", as in "hamburger” or “cheeseburger"). Since it is pediatric practice, kudos will be given to designs that implement a little joke into the design - but hopefully in a small or hidden way (such as putting something like a cheeseburger on the back of the card, or hiding it an an abstract way).

Thank you!

Please make a design that incorporates colors. It should be fun! Not too serious. It does not have to follow the color scheme of the logos.

```html
<!DOCTYPE html>
<html lang="en">
<head>
<meta charset="utf-8">
<title>Copper Fern Pediatric Dentistry – Business Card</title>
<link href="https://fonts.googleapis.com/css2?family=Open+Sans:wght@300;400;600;700&display=swap" rel="stylesheet">
<style>
  :root {
    --page: #e9e9e9;
    --ink: #111111;
    --card-dark: #373c39;
    --burger-tone: #424844;
    --green-pale: #a9c7a3;
    --green-soft: #86b47f;
    --green-mid: #5ba266;
    --green-deep: #358150;
    --outline: #363b38;
    --text-light: #f2f2f2;
    --text-green: #a9cf9f;
    --brand-grey: #3b3f3d;
  }
  * { margin: 0; padding: 0; box-sizing: border-box; }
  html, body {
    width: 1200px; height: 1200px; overflow: hidden;
    background: var(--page);
    font-family: "Open Sans", Arial, sans-serif;
  }
  .canvas { position: relative; width: 1200px; height: 1200px; }
  .brand-mark {
    position: absolute; top: 180px; right: 110px; text-align: right;
    color: var(--brand-grey);
  }
  .brand-mark .brand-name { font-size: 34px; font-weight: 600; letter-spacing: 1px; }
  .brand-mark .brand-tag { font-size: 11px; font-weight: 600; letter-spacing: 4px; margin-top: 4px; }
  .card { position: absolute; width: 500px; height: 480px; }
  .card svg { display: block; filter: drop-shadow(0 8px 14px rgba(0,0,0,.18)); }
  .card-back { left: 150px; top: 150px; }
  .card-front { left: 560px; top: 560px; }
  .side-label {
    position: absolute; font-size: 26px; font-weight: 700; color: var(--ink);
  }
  .label-back { left: 700px; top: 440px; }
  .label-front { left: 420px; top: 990px; }
</style>
</head>
<body>
<main class="canvas">

  <div class="brand-mark">
    <div class="brand-name">Copper Fern</div>
    <div class="brand-tag">PEDIATRIC DENTISTRY</div>
  </div>

  <section class="card card-back" aria-label="Card back">
    <svg width="500" height="480" viewBox="0 0 500 480">
      <defs>
        <clipPath id="tooth-back">
          <path d="M250 70 C300 20 360 0 400 10 C470 30 500 110 495 220 C490 330 460 420 420 460 C390 480 360 470 340 430 C320 390 300 360 250 360 C200 360 180 390 160 430 C140 470 110 480 80 460 C40 420 10 330 5 220 C0 110 30 30 100 10 C140 0 200 20 250 70 Z"/>
        </clipPath>
        <linearGradient id="back-fill" x1="0" y1="0" x2="1" y2="1">
          <stop offset="0" stop-color="#a9c7a3"/>
          <stop offset="0.55" stop-color="#86b47f"/>
          <stop offset="1" stop-color="#358150"/>
        </linearGradient>
      </defs>
      <g clip-path="url(#tooth-back)">
        <rect width="500" height="480" fill="url(#back-fill)" role="img" aria-label="Large green tooth shaped brand pattern"/>
      </g>
      <text x="250" y="215" text-anchor="middle" font-family="Open Sans, Arial, sans-serif" font-size="44" font-weight="600" fill="#363b38">Copper Fern</text>
    </svg>
  </section>

  <span class="side-label label-back">Back</span>

  <section class="card card-front" aria-label="Card front">
    <svg width="500" height="480" viewBox="0 0 500 480">
      <defs>
        <clipPath id="tooth-front">
          <path d="M250 70 C300 20 360 0 400 10 C470 30 500 110 495 220 C490 330 460 420 420 460 C390 480 360 470 340 430 C320 390 300 360 250 360 C200 360 180 390 160 430 C140 470 110 480 80 460 C40 420 10 330 5 220 C0 110 30 30 100 10 C140 0 200 20 250 70 Z"/>
        </clipPath>
        <radialGradient id="burger-fill" cx="0.5" cy="0.5" r="0.5">
          <stop offset="0" stop-color="#464c48"/>
          <stop offset="1" stop-color="#373c39"/>
        </radialGradient>
      </defs>
      <g clip-path="url(#tooth-front)">
        <rect width="500" height="480" fill="var(--card-dark)"/>
        <ellipse cx="410" cy="110" rx="120" ry="120" fill="url(#burger-fill)" role="img" aria-label="Faint hamburger illustration"/>
      </g>

      <g font-family="Open Sans, Arial, sans-serif">
        <circle cx="110" cy="98" r="6" fill="var(--green-soft)"/>
        <text x="124" y="106" font-size="26" font-weight="600" fill="var(--text-light)">Copper Fern</text>
        <text x="124" y="124" font-size="9" font-weight="600" letter-spacing="3" fill="var(--text-light)">PEDIATRIC DENTISTRY</text>

        <text x="110" y="180" font-size="22" font-weight="600" fill="var(--text-green)">Wren Tolvan</text>
        <text x="110" y="204" font-size="18" font-weight="300" fill="var(--text-light)">Dentistry</text>

        <g font-size="15" font-weight="300" fill="var(--text-light)">
          <circle cx="118" cy="245" r="7" fill="none" stroke="var(--text-green)" stroke-width="1.3"/>
          <circle cx="118" cy="243.5" r="2" fill="var(--text-green)"/>
          <text x="134" y="250">4810 Marrow Lane Ste 12</text>

          <circle cx="118" cy="272" r="7" fill="none" stroke="var(--text-green)" stroke-width="1.3"/>
          <path d="M115 269 q0 6 6 6" fill="none" stroke="var(--text-green)" stroke-width="1.5"/>
          <text x="134" y="277">+1 555-014-2210</text>

          <circle cx="118" cy="299" r="7" fill="none" stroke="var(--text-green)" stroke-width="1.3"/>
          <rect x="114" y="296" width="8" height="6" fill="none" stroke="var(--text-green)" stroke-width="1"/>
          <path d="M114 296 l4 3 l4 -3" fill="none" stroke="var(--text-green)" stroke-width="1"/>
          <text x="134" y="304">info@copperfern.com</text>
        </g>
        <text x="134" y="334" font-size="16" font-weight="400" fill="var(--text-green)">www.copperfern.com</text>
      </g>
    </svg>
  </section>

  <span class="side-label label-front">Front</span>

</main>
</body>
</html>
```